Falcrest security business card

Looking for a business card for my security company

Target Market(s)

Security

Industry/Entity Type

Security

Contact Information for Business Card

Name - Gil Marston. Title - General manager - direct 314 862.4490 website www. falcrestsecurityservices.example email - gil@ falcrestsecurityservices.example

Requirements
Must have
• Logo attached

```html
<!DOCTYPE html>
<html lang="en">
<head>
<meta charset="utf-8">
<title>Falcrest Security – Business Card</title>
<link rel="stylesheet" href="https://fonts.googleapis.com/css2?family=Montserrat:wght@800&family=Arimo:wght@400&display=swap">
<style>
  :root {
    --backdrop: #2a2a2a;
    --card: #1f1f1f;
    --gold: #c9963f;
    --gold-light: #e8c57a;
    --text: #f2f2f2;
  }
  html, body {
    margin: 0;
    width: 1200px;
    height: 900px;
    overflow: hidden;
    background: var(--backdrop);
  }
  .canvas {
    width: 1200px;
    height: 900px;
    display: flex;
    align-items: center;
    justify-content: center;
  }
  .business-card {
    position: relative;
    width: 1050px;
    height: 600px;
    background: var(--card);
    border: 3px solid var(--gold);
    box-sizing: border-box;
    display: flex;
    align-items: center;
  }
  .brand {
    width: 520px;
    display: flex;
    align-items: center;
    justify-content: center;
  }
  .brand-name {
    font-family: "Montserrat", sans-serif;
    font-weight: 800;
    font-size: 78px;
    letter-spacing: 2px;
    text-transform: uppercase;
    color: var(--gold);
    margin: 0;
  }
  .divider {
    width: 1px;
    height: 230px;
    background: var(--gold);
    opacity: 0.8;
  }
  .contact {
    padding-left: 50px;
    font-family: "Arimo", sans-serif;
    color: var(--text);
  }
  .contact-name {
    font-family: "Montserrat", sans-serif;
    font-weight: 800;
    font-size: 34px;
    letter-spacing: 1px;
    text-transform: uppercase;
    color: var(--gold);
    margin: 0;
  }
  .contact-title {
    font-size: 24px;
    margin: 4px 0 26px;
  }
  .contact-list {
    list-style: none;
    margin: 0;
    padding: 0;
  }
  .contact-item {
    display: flex;
    align-items: center;
    gap: 12px;
    font-size: 22px;
    line-height: 38px;
  }
  .contact-icon {
    width: 18px;
    height: 18px;
    flex: none;
    fill: var(--gold-light);
  }
</style>
</head>
<body>
<main class="canvas">
  <section class="business-card">
    <div class="brand">
      <h1 class="brand-name">Falcrest</h1>
    </div>
    <div class="divider"></div>
    <div class="contact">
      <h2 class="contact-name">Gil Marston</h2>
      <p class="contact-title">General manager</p>
      <ul class="contact-list">
        <li class="contact-item">
          <svg class="contact-icon" viewBox="0 0 24 24" aria-hidden="true"><path d="M6.6 10.8a15.1 15.1 0 0 0 6.6 6.6l2.2-2.2a1 1 0 0 1 1-.25 11.4 11.4 0 0 0 3.6.57 1 1 0 0 1 1 1V20a1 1 0 0 1-1 1A17 17 0 0 1 3 4a1 1 0 0 1 1-1h3.5a1 1 0 0 1 1 1c0 1.25.2 2.45.57 3.57a1 1 0 0 1-.25 1z"/></svg>
          <span>314 862.4490</span>
        </li>
        <li class="contact-item">
          <svg class="contact-icon" viewBox="0 0 24 24" aria-hidden="true"><path d="M2 5h20v14H2z M4 7v.5l8 5.5 8-5.5V7l-8 5.5z" fill-rule="evenodd"/></svg>
          <span>gil@falcrestsecurityservices.example</span>
        </li>
        <li class="contact-item">
          <svg class="contact-icon" viewBox="0 0 24 24" aria-hidden="true"><circle cx="12" cy="12" r="10"/><path d="M2 12h20M12 2c3 3 3 17 0 20M12 2c-3 3-3 17 0 20" stroke="#1f1f1f" stroke-width="1.5" fill="none"/></svg>
          <span>www.falcrestsecurityservices.example</span>
        </li>
      </ul>
    </div>
  </section>
</main>
</body>
</html>
```